The homepage of a website

This is a simple project that should take from you a few minutes as what is needed is the design of the homepage only, the details are in the attached zip file

Please note that KBLTA board required a special tailored design where they got some parts from the different posted designs, if you are interested please follow the instructions in the below URL and submit your new updated designs as per the instructions (P.S. I will mark the project as guaranteed as an assurance to all of you)

http://quorvanet.com/Projects/KBLTA/Design.jpg

Please note that KBLTA board required a special tailored design where they got some parts from the different posted designs, if you are interested please follow the instructions in the below URL and submit your new updated designs as per the instructions (P.S. I will mark the project as guaranteed as an assurance to all of you) http://quorvanet.com/Projects/KBLTA/Design.jpg

```html
<!DOCTYPE html>
<html lang="en">
<head>
<meta charset="utf-8">
<title>KBLTA – Home</title>
<link href="https://fonts.googleapis.com/css2?family=Source+Sans+3:wght@400;600&display=swap" rel="stylesheet">
<style>
:root{
  --navy:#243e6b;
  --navy-btn:#34416f;
  --white:#ffffff;
  --page:#ffffff;
  --band:#ececec;
  --text:#5c5c5c;
  --muted:#c9c9c9;
  --line:#9a9a9a;
  --hero-a:#c6d3e0;
  --hero-b:#a9bccf;
  --hist-a:#b59ad0;
  --hist-b:#8a6cb8;
}
*{margin:0;padding:0;box-sizing:border-box}
html,body{width:762px;height:1200px;overflow:hidden;background:var(--page)}
body{font-family:"Source Sans 3",sans-serif;color:var(--text);position:relative}
.abs{position:absolute}
.hero{left:0;top:0;width:762px;height:419px;background:linear-gradient(160deg,var(--hero-a),var(--hero-b))}
.brand{left:163px;top:60px;display:flex;align-items:center;gap:12px}
.brand-mark{width:70px;height:70px;border-radius:50%;border:2px solid var(--navy)}
.brand-name{font-size:30px;font-weight:600;color:var(--navy);letter-spacing:1px}
.society{right:165px;top:104px;width:320px;text-align:right;font-size:19px;font-weight:600;color:var(--navy);line-height:1.3}
.hex-btn{width:63px;height:69px;text-align:center;color:var(--white)}
.hex-btn svg{position:absolute;left:0;top:0}
.hex-btn span{position:absolute;left:0;right:0;top:46px;font-size:6.5px}
.nav{left:0;top:419px;width:762px;height:53px;background:var(--white)}
.nav-logo{left:164px;top:15px;font-size:12px;font-weight:600;color:var(--navy);display:flex;align-items:center;gap:4px}
.nav-logo i{width:10px;height:10px;border-radius:50%;background:var(--navy);display:block}
.nav ul{position:absolute;right:164px;top:25px;list-style:none;display:flex;gap:11px;font-size:6.6px;color:#444}
.nav li.active{color:var(--navy);font-weight:600}
.features{left:0;top:472px;width:762px;height:303px;background:var(--band)}
.feature{width:110px;text-align:center}
.feature svg{display:block;margin:0 auto}
.feature h3{font-size:9px;font-weight:400;margin-top:18px;color:var(--text)}
.feature p{font-size:5.3px;line-height:11px;margin-top:12px;color:#444}
.search{left:0;top:775px;width:762px;height:188px}
.search h2{position:absolute;left:0;right:0;top:62px;text-align:center;font-size:17px;font-weight:600;color:var(--text)}
.search-input{left:163px;top:105px;width:336px;height:28px;border:1px solid var(--line);background:var(--white)}
.search-btn{left:511px;top:105px;width:86px;height:28px;background:var(--navy-btn);color:var(--white);font-size:7.5px;font-weight:600;display:flex;align-items:center;justify-content:center;border-bottom:1px solid #7a3a60}
.history{left:0;top:963px;width:762px;height:237px;background:linear-gradient(120deg,var(--hist-b),var(--hist-a) 55%,#d8d6e6)}
.history h2{position:absolute;left:0;right:0;top:146px;text-align:center;font-size:18.5px;font-weight:600;color:var(--white)}
</style>
</head>
<body>
<section class="abs hero" role="img" aria-label="Photo of a surgeon's gloved hands examining a patient's face"></section>

<div class="abs brand"><i class="brand-mark"></i><span class="brand-name">KBLTA</span></div>
<div class="abs society">The Kelbaran Society of Plastic<br>&amp; Restorative Surgeons</div>

<svg width="0" height="0" style="position:absolute"><defs>
<polygon id="hex" points="32,2 61,18.5 61,51.5 32,68 3,51.5 3,18.5"/>
</defs></svg>

<a class="abs hex-btn" style="left:164px;top:284px">
<svg width="63" height="69" viewBox="0 0 64 70" fill="none" stroke="#fff" stroke-width="1.6" stroke-linejoin="round"><use href="#hex"/><circle cx="32" cy="29" r="6"/><circle cx="32" cy="29" r="2.5"/><path d="M32 20v3M32 35v3M23 29h3M38 29h3M25.6 22.6l2 2M36.4 33.4l2 2M25.6 35.4l2-2M36.4 24.6l2-2"/></svg>
<span>languag</span></a>
<a class="abs hex-btn" style="left:238px;top:284px">
<svg width="63" height="69" viewBox="0 0 64 70" fill="none" stroke="#fff" stroke-width="1.6" stroke-linejoin="round"><use href="#hex"/><circle cx="32" cy="25" r="6"/><path d="M23 38c0-5 4-7 9-7s9 2 9 7z"/></svg>
<span>Member</span></a>
<a class="abs hex-btn" style="left:462px;top:284px">
<svg width="63" height="69" viewBox="0 0 64 70" fill="none" stroke="#fff" stroke-width="1.6" stroke-linejoin="round"><use href="#hex"/><path d="M25 37l2-7 11-11 5 5-11 11z M36 21l5 5"/></svg>
<span>History</span></a>
<a class="abs hex-btn" style="left:535px;top:284px">
<svg width="63" height="69" viewBox="0 0 64 70" fill="none" stroke="#fff" stroke-width="1.6" stroke-linejoin="round"><use href="#hex"/><path d="M22 29l20-9-6 19-4-7z M32 32l10-12"/></svg>
<span>Contact</span></a>
<svg class="abs" style="left:365px;top:352px" width="32" height="35" viewBox="0 0 64 70" fill="none" stroke="#fff" stroke-width="2.4" stroke-linejoin="round"><use href="#hex"/><path d="M24 31l8 8 8-8"/></svg>

<nav class="abs nav">
<div class="abs nav-logo"><i></i>KBLTA</div>
<ul><li>HOME</li><li class="active">ABOUT</li><li>MEMBERS</li><li>EVENTS</li><li>HISTORY</li><li>INFORMATION</li><li>CONTACT</li></ul>
</nav>

<section class="abs features">
<div class="abs feature" style="left:158px;top:64px">
<svg width="66" height="71" viewBox="0 0 64 70" fill="none" stroke="#243e6b" stroke-width="1.6" stroke-linejoin="round"><use href="#hex"/><path d="M32 44c-9-6-13-10-13-15a6 6 0 0 1 13-2 6 6 0 0 1 13 2c0 5-4 9-13 15z"/></svg>
<h3>Membership</h3>
<p>Fusce facilisis velit libero, nec<br>dignissim lacus sagittis non.<br>Sed nec porta ante. Pellentesque<br>habitant morbi tristique senectus et.</p></div>
<div class="abs feature" style="left:270px;top:64px">
<svg width="66" height="71" viewBox="0 0 64 70" fill="none" stroke="#c9c9c9" stroke-width="1.4" stroke-linejoin="round"><use href="#hex"/><path d="M21 30l5-6h12l5 6-11 13z M21 30h22 M27 30l5 13 5-13 M26 24l3 6 3-6 3 6 3-6"/></svg>
<h3>Values</h3>
<p>Fusce facilisis velit libero, nec<br>dignissim lacus sagittis non.<br>Sed nec porta ante. Pellentesque<br>habitant morbi tristique senectus et.</p></div>
<div class="abs feature" style="left:382px;top:64px">
<svg width="66" height="71" viewBox="0 0 64 70" fill="none" stroke="#c9c9c9" stroke-width="1.4" stroke-linejoin="round"><use href="#hex"/><path d="M24 24h16v4H24z M25 28l2 16h10l2-16 M26 33h12"/></svg>
<h3>Laws</h3>
<p>Fusce facilisis velit libero, nec<br>dignissim lacus sagittis non.<br>Sed nec porta ante. Pellentesque<br>habitant morbi tristique senectus et.</p></div>
<div class="abs feature" style="left:493px;top:64px">
<svg width="66" height="71" viewBox="0 0 64 70" fill="none" stroke="#c9c9c9" stroke-width="1.4" stroke-linejoin="round"><use href="#hex"/><rect x="25" y="22" width="14" height="24" rx="2"/><path d="M25 26h14M25 41h14"/></svg>
<h3>Links</h3>
<p>Fusce facilisis velit libero, nec<br>dignissim lacus sagittis non.<br>Sed nec porta ante. Pellentesque<br>habitant morbi tristique senectus et.</p></div>
</section>

<section class="abs search">
<h2>Search</h2>
<div class="abs search-input"></div>
<div class="abs search-btn">Search</div>
</section>

<section class="abs history" role="img" aria-label="Photo of smiling medical staff in a hospital ward, tinted purple">
<svg class="abs" style="left:349px;top:21px" width="63" height="69" viewBox="0 0 64 70" fill="none" stroke="#fff" stroke-width="1.6" stroke-linejoin="round"><use href="#hex"/><path d="M20 29l12-5 12 5-12 5z M25 31v7c4 3 10 3 14 0v-7 M44 29v8"/></svg>
<h2>Our history</h2>
</section>
</body>
</html>
```